Website for Apartment Rental in Prague

I would like to create designs of my website focused on luxury apartment rentals in Prague, Czech Republic. I created initial mock-ups, They are all attached. I need to design homepage and subpage. The mock-ups were created by combining elements from different websites that I liked but I need you to create a design that is unique and original. The attached files a only a guidance for the structure of the website but not for the design. Try to be creative.

Industry/Entity Type

Apartment

```html
<!DOCTYPE html>
<html lang="en">
<head>
<meta charset="utf-8">
<title>Lumen Residences Prague</title>
<link href="https://fonts.googleapis.com/css2?family=Oswald:wght@400;500&family=Roboto:wght@300;400;500;700&display=swap" rel="stylesheet">
<style>
:root{
  --brown:#a8705a;
  --brown-dark:#946049;
  --footer:#a9745b;
  --ink:#222;
  --text:#555;
  --muted:#888;
  --line:#dcdcdc;
  --soft:#f6f6f6;
  --topbar:#f3f3f3;
  --white:#fff;
}
*{box-sizing:border-box;margin:0;padding:0}
html,body{width:1200px;height:3629px;overflow:hidden}
body{position:relative;font-family:"Roboto",Arial,sans-serif;color:var(--text);background:var(--white)}
.abs{position:absolute}
.center{text-align:center}

/* top bar */
.topbar{left:0;top:0;width:1200px;height:34px;background:var(--topbar);font-size:12px;color:#555}
.topbar .item{top:0;height:34px;display:flex;align-items:center;gap:6px}
.topbar svg{width:12px;height:12px;fill:var(--brown)}
.lang{left:1042px;top:4px;width:46px;height:26px;background:#ddd;display:flex;align-items:center;justify-content:center;font-size:12px}

/* header */
.header{left:0;top:34px;width:1200px;height:72px;background:var(--white)}
.brand{left:110px;top:46px;width:120px;text-align:center;color:var(--brown);font-size:18px;font-weight:500;line-height:20px}
.brand small{display:block;font-size:10px;letter-spacing:3px;color:#333}
.nav{right:110px;top:34px;height:72px;display:flex;align-items:center;gap:28px;font-size:12px;font-weight:500;color:#333;text-transform:uppercase}

/* hero */
.hero-photo{left:0;top:106px;width:1200px;height:559px;background:linear-gradient(100deg,#6b5a4c 0%,#c9c2b6 30%,#e8e4dc 50%,#8d8f7c 70%,#5a4c40 100%)}
.hero-box{left:344px;top:235px;width:516px;height:237px;background:rgba(40,40,40,.45)}
.hero-title{left:344px;top:272px;width:516px;font-family:"Oswald",sans-serif;font-size:40px;color:var(--white);letter-spacing:1px}
.hero-text{left:384px;top:332px;width:436px;font-size:13px;line-height:19px;color:#eee}
.btn{background:var(--brown);color:var(--white);font-size:12px;font-weight:700;text-transform:uppercase;display:flex;align-items:center;justify-content:center;border-radius:3px}
.hero-btn{left:550px;top:411px;width:104px;height:41px}

/* booking */
.booking{left:145px;top:605px;width:945px;height:198px;background:var(--white);box-shadow:0 2px 12px rgba(0,0,0,.12);border-radius:3px}
.field-label{font-size:11px;color:#444}
.field{height:39px;border:1px solid var(--line);background:var(--white)}
.cal{position:absolute;right:10px;top:12px;width:14px;height:14px}
.or{left:580px;top:708px;width:40px;font-size:11px;color:#555}
.select{left:484px;top:740px;width:235px;height:37px;border:1px solid var(--line);font-size:12px;color:#444;padding-left:10px;display:flex;align-items:center}
.select svg{position:absolute;right:10px;top:14px}

/* headings */
.h2{left:0;width:1200px;font-size:22px;font-weight:400;color:var(--ink);letter-spacing:.5px;text-transform:uppercase}
.divider{left:570px;width:60px;height:1px;background:#ccc}
.para{font-size:13px;line-height:22px;color:var(--text)}

/* welcome */
.welcome-mark{left:0;top:852px;width:1200px;font-size:18px;color:var(--brown);font-weight:500}

/* interiors */
.interiors{left:0;top:1065px;width:1200px;height:927px;background:linear-gradient(#f3f3f3,#fff 30%)}
.card{width:300px;height:300px}
.card .photo{position:absolute;inset:0}
.card .shade{position:absolute;left:0;right:0;bottom:0;height:130px;background:linear-gradient(transparent,rgba(0,0,0,.85))}
.card .info{position:absolute;left:18px;bottom:14px;color:var(--white)}
.stars{display:flex;gap:2px}
.stars svg{width:11px;height:11px;fill:#f2a32b}
.card h3{font-size:14px;font-weight:500;margin-top:4px}
.card .loc{font-size:10px;color:#ddd;margin-top:3px;display:flex;align-items:center;gap:4px}
.card .price{font-size:12px;margin-top:8px}
.card .price b{font-size:17px;font-weight:700}
.photo-hall{background:linear-gradient(160deg,#4a3a2e,#8c7f6c 40%,#d2cfc6 60%,#3a302a)}
.photo-sea{background:linear-gradient(#3e5a80,#7c9cc0 45%,#9fb7cf 60%,#30455e)}
.photo-room{background:linear-gradient(150deg,#2b2b2b,#5a5a58 45%,#8c8b86 60%,#222)}

/* services */
.services{left:0;top:1992px;width:1200px;height:428px;background:var(--soft)}
.service{width:300px;height:80px}
.service .icon{position:absolute;left:0;top:0;width:48px;height:48px;border-radius:50%;background:var(--brown);display:flex;align-items:center;justify-content:center}
.service .icon svg{width:22px;height:22px;fill:none;stroke:var(--white);stroke-width:2}
.service h4{position:absolute;left:60px;top:2px;font-size:16px;font-weight:500;color:var(--brown);text-transform:uppercase}
.service p{position:absolute;left:60px;top:26px;width:230px;font-size:12px;line-height:19px;color:var(--text)}

/* testimonial */
.testi-bg{left:0;top:2420px;width:1200px;height:590px;background:linear-gradient(100deg,#3a3530,#6d645a 40%,#4c463f 70%,#2e2a26)}
.testi-title{top:2474px;color:var(--white)}
.quote-box{left:259px;top:2572px;width:571px;height:235px;border:1px solid rgba(255,255,255,.3);background:rgba(255,255,255,.06);border-radius:4px}
.quote-mark{left:256px;top:2580px}
.quote-text{left:290px;top:2622px;width:510px;font-size:15px;font-style:italic;line-height:26px;color:var(--white)}
.avatar{left:411px;top:2827px;width:102px;height:102px;border-radius:50%;background:radial-gradient(#e9d6bd,#b79a7a);border:3px solid var(--white)}
.cust-name{left:528px;top:2868px;font-size:14px;color:var(--white)}
.couple{left:799px;top:2565px;width:401px;height:445px;background:linear-gradient(160deg,#c79a5a,#8f6b4c 40%,#e0d6c9 70%,#3c3c48)}

/* newsletter */
.newsletter{left:0;top:3010px;width:1200px;height:293px;background:#f2f2f2}
.email{left:249px;top:3206px;width:545px;height:39px;border-radius:20px;background:var(--white);font-size:11px;color:#aaa;padding-left:22px;display:flex;align-items:center}
.subscribe{left:806px;top:3206px;width:145px;height:39px;border-radius:20px}

/* footer */
.footer{left:0;top:3303px;width:1200px;height:326px;background:var(--footer);color:var(--white)}
.fh{top:3350px;font-size:21px;font-weight:500;text-transform:uppercase}
.contact-row{display:flex;gap:12px;font-size:12px;line-height:17px}
.contact-row svg{width:14px;height:14px;fill:var(--white);flex:none;margin-top:2px}
.links{font-size:12px;line-height:26px}
.gal{top:3402px;width:121px;height:126px}
.g1{background:linear-gradient(#dfe6ea,#8fa4b4)}
.g2{background:linear-gradient(#2f6da4,#8bb7d3 50%,#8c6a4c)}
.g3{background:linear-gradient(#78a6c8,#4f7a3a 55%,#a67b52)}
.foot-line{left:0;top:3564px;width:1200px;height:1px;background:rgba(255,255,255,.3)}
.copy{left:0;top:3586px;width:1200px;font-size:11px}
</style>
</head>
<body>

<!-- top bar -->
<div class="abs topbar">
  <div class="abs item" style="left:405px"><svg viewBox="0 0 24 24"><path d="M6.6 10.8a15 15 0 006.6 6.6l2.2-2.2c.3-.3.7-.4 1-.2 1.1.4 2.3.6 3.6.6.6 0 1 .4 1 1V20c0 .6-.4 1-1 1A17 17 0 013 4c0-.6.4-1 1-1h3.5c.6 0 1 .4 1 1 0 1.3.2 2.5.6 3.6.1.3 0 .7-.2 1z"/></svg><span style="color:#333;font-weight:500">+420 600 123 456</span></div>
  <div class="abs item" style="left:560px"><svg viewBox="0 0 24 24"><path d="M2 5h20v14H2z M2 5l10 8 10-8" fill="none" stroke="#a8705a" stroke-width="2"/></svg>booking@lumenstay.example</div>
  <div class="abs item" style="left:790px"><svg viewBox="0 0 24 24"><path d="M12 21l-8-8a5 5 0 018-6 5 5 0 018 6z"/></svg>Our Hospitality</div>
  <div class="abs item" style="left:912px"><svg viewBox="0 0 24 24"><path d="M12 2a7 7 0 00-7 7c0 5 7 13 7 13s7-8 7-13a7 7 0 00-7-7zm0 9.5A2.5 2.5 0 1112 6a2.5 2.5 0 010 5.5z"/></svg>Discover Prague</div>
  <div class="abs lang">EN ▾</div>
</div>

<!-- header -->
<div class="abs header"></div>
<div class="abs brand">Lumen<small>RESIDENCES</small><small style="font-weight:700">PRAGUE</small></div>
<nav class="abs nav">
  <span>Apartments</span><span>Location</span><span>Services</span><span>Gallery</span><span>News</span><span>Exclusive Offers &amp; Tours</span><span>For Families</span><span>Contact</span>
</nav>

<!-- hero -->
<div class="abs hero-photo" role="img" aria-label="Bright living room with fireplace, staircase and sofa by large windows"></div>
<div class="abs hero-box"></div>
<h1 class="abs hero-title center" style="font-weight:400">BEING HOME IN PRAGUE</h1>
<p class="abs hero-text center">Ctincidunt ut laoreet dolore magna aliquam erat volutpat. Ut wisi enim ad minim veniam, quis nostrud exerci tation ullamcorper suscipit lobortis nisl ut aliquip.</p>
<div class="abs btn hero-btn">Book Now</div>

<!-- booking -->
<div class="abs booking"></div>
<div class="abs field-label" style="left:165px;top:634px">Check in Date</div>
<div class="abs field" style="left:165px;top:653px;width:137px"><svg class="cal" viewBox="0 0 14 14"><rect x="1" y="2" width="12" height="11" fill="none" stroke="#bbb"/><path d="M1 5h12" stroke="#bbb"/></svg></div>
<div class="abs field-label" style="left:312px;top:634px">Check out Date</div>
<div class="abs field" style="left:312px;top:653px;width:138px"><svg class="cal" viewBox="0 0 14 14"><rect x="1" y="2" width="12" height="11" fill="none" stroke="#bbb"/><path d="M1 5h12" stroke="#bbb"/></svg></div>
<div class="abs field-label" style="left:460px;top:634px">Adults</div>
<div class="abs field" style="left:460px;top:653px;width:70px"></div>
<div class="abs field-label" style="left:540px;top:634px">Children</div>
<div class="abs field" style="left:540px;top:653px;width:70px"></div>
<div class="abs field-label" style="left:620px;top:634px">Infants</div>
<div class="abs field" style="left:620px;top:653px;width:70px"></div>
<div class="abs field-label" style="left:700px;top:634px">Promotional Code</div>
<div class="abs field" style="left:700px;top:653px;width:174px"></div>
<div class="abs btn" style="left:890px;top:653px;width:146px;height:36px;font-size:11px">Check Availability</div>
<div class="abs or center">OR</div>
<div class="abs select">Select Rental Unit<svg width="12" height="8" viewBox="0 0 12 8"><path d="M1 1l5 5 5-5" fill="none" stroke="#555" stroke-width="1.5"/></svg></div>

<!-- welcome -->
<div class="abs welcome-mark center">Lumen</div>
<h2 class="abs h2 center" style="top:884px">Welcome Lumen Residences Prague</h2>
<div class="abs divider" style="top:924px"></div>
<p class="abs para center" style="left:189px;top:950px;width:823px">Ctincidunt ut laoreet dolore magna aliquam erat volutpat. Ut wisi enim ad mini m veniam, quis nostrud exerci tation suscipit lobortis nisl ut aliquip. Ctincidunt ut laoreet dolore magna aliquam erat volutpat. Ut wisi enim ad mini m veniam, quis nostrud exerci tation ullamcorperullamcorper suscipit lobortis nisl ut aliquip. Ctincidunt ut laoreet dolore magna.</p>

<!-- interiors -->
<div class="abs interiors"></div>
<h2 class="abs h2 center" style="top:1124px">Interiors Designed</h2>
<p class="abs para center" style="left:130px;top:1185px;width:940px">Ctincidunt ut laoreet dolore magna aliquam erat volutpat. Ut wisi enim ad mini m veniam, quis nostrud exerci tation suscipit lobortis nisl ut aliquip. Ctincidunt ut laoreet dolore magna aliquam erat volutpat. Ut wisi enim ad mini m veniam, quis nostrud exerci tation ullamcorperullamcorper suscipit lobortis nisl ut aliquip. Ctincidunt ut laoreet dolore magna.</p>

<div class="abs card" style="left:111px;top:1297px"><div class="photo photo-hall" role="img" aria-label="Modern apartment lobby with chandelier"></div><div class="shade"></div><div class="info"><div class="stars"><svg viewBox="0 0 10 10"><path d="M5 0l1.5 3.3 3.5.4-2.6 2.4.7 3.5L5 7.8 1.9 9.6l.7-3.5L0 3.7l3.5-.4z"/></svg><svg viewBox="0 0 10 10"><path d="M5 0l1.5 3.3 3.5.4-2.6 2.4.7 3.5L5 7.8 1.9 9.6l.7-3.5L0 3.7l3.5-.4z"/></svg><svg viewBox="0 0 10 10"><path d="M5 0l1.5 3.3 3.5.4-2.6 2.4.7 3.5L5 7.8 1.9 9.6l.7-3.5L0 3.7l3.5-.4z"/></svg><svg viewBox="0 0 10 10"><path d="M5 0l1.5 3.3 3.5.4-2.6 2.4.7 3.5L5 7.8 1.9 9.6l.7-3.5L0 3.7l3.5-.4z"/></svg><svg viewBox="0 0 10 10"><path d="M5 0l1.5 3.3 3.5.4-2.6 2.4.7 3.5L5 7.8 1.9 9.6l.7-3.5L0 3.7l3.5-.4z"/></svg></div><h3>Brand New Modern Apartment</h3><div class="loc"><svg width="8" height="10" viewBox="0 0 8 10"><path d="M4 0a3.5 3.5 0 00-3.5 3.5C.5 6 4 10 4 10s3.5-4 3.5-6.5A3.5 3.5 0 004 0z" fill="#ddd"/></svg>Unbeatable Location</div><div class="price">From <b>$150.0</b> &nbsp;/Per Night</div></div></div>

<div class="abs card" style="left:450px;top:1297px"><div class="photo photo-sea" role="img" aria-label="Sea view at dusk from the apartment terrace"></div><div class="shade"></div><div class="info"><div class="stars"><svg viewBox="0 0 10 10"><path d="M5 0l1.5 3.3 3.5.4-2.6 2.4.7 3.5L5 7.8 1.9 9.6l.7-3.5L0 3.7l3.5-.4z"/></svg><svg viewBox="0 0 10 10"><path d="M5 0l1.5 3.3 3.5.4-2.6 2.4.7 3.5L5 7.8 1.9 9.6l.7-3.5L0 3.7l3.5-.4z"/></svg><svg viewBox="0 0 10 10"><path d="M5 0l1.5 3.3 3.5.4-2.6 2.4.7 3.5L5 7.8 1.9 9.6l.7-3.5L0 3.7l3.5-.4z"/></svg><svg viewBox="0 0 10 10"><path d="M5 0l1.5 3.3 3.5.4-2.6 2.4.7 3.5L5 7.8 1.9 9.6l.7-3.5L0 3.7l3.5-.4z"/></svg><svg viewBox="0 0 10 10"><path d="M5 0l1.5 3.3 3.5.4-2.6 2.4.7 3.5L5 7.8 1.9 9.6l.7-3.5L0 3.7l3.5-.4z"/></svg></div><h3>Brand New Modern Apartment</h3><div class="loc"><svg width="8" height="10" viewBox="0 0 8 10"><path d="M4 0a3.5 3.5 0 00-3.5 3.5C.5 6 4 10 4 10s3.5-4 3.5-6.5A3.5 3.5 0 004 0z" fill="#ddd"/></svg>Unbeatable Location</div><div class="price">From <b>$150.0</b> &nbsp;/Per Night</div></div></div>

<div class="abs card" style="left:787px;top:1297px"><div class="photo photo-room" role="img" aria-label="Dark modern living room with sofa"></div><div class="shade"></div><div class="info"><div class="stars"><svg viewBox="0 0 10 10"><path d="M5 0l1.5 3.3 3.5.4-2.6 2.4.7 3.5L5 7.8 1.9 9.6l.7-3.5L0 3.7l3.5-.4z"/></svg><svg viewBox="0 0 10 10"><path d="M5 0l1.5 3.3 3.5.4-2.6 2.4.7 3.5L5 7.8 1.9 9.6l.7-3.5L0 3.7l3.5-.4z"/></svg><svg viewBox="0 0 10 10"><path d="M5 0l1.5 3.3 3.5.4-2.6 2.4.7 3.5L5 7.8 1.9 9.6l.7-3.5L0 3.7l3.5-.4z"/></svg><svg viewBox="0 0 10 10"><path d="M5 0l1.5 3.3 3.5.4-2.6 2.4.7 3.5L5 7.8 1.9 9.6l.7-3.5L0 3.7l3.5-.4z"/></svg><svg viewBox="0 0 10 10"><path d="M5 0l1.5 3.3 3.5.4-2.6 2.4.7 3.5L5 7.8 1.9 9.6l.7-3.5L0 3.7l3.5-.4z"/></svg></div><h3>Brand New Modern Apartment</h3><div class="loc"><svg width="8" height="10" viewBox="0 0 8 10"><path d="M4 0a3.5 3.5 0 00-3.5 3.5C.5 6 4 10 4 10s3.5-4 3.5-6.5A3.5 3.5 0 004 0z" fill="#ddd"/></svg>Unbeatable Location</div><div class="price">From <b>$150.0</b> &nbsp;/Per Night</div></div></div>

<div class="abs card" style="left:111px;top:1631px"><div class="photo photo-hall" role="img" aria-label="Modern apartment lobby with chandelier"></div><div class="shade"></div><div class="info"><div class="stars"><svg viewBox="0 0 10 10"><path d="M5 0l1.5 3.3 3.5.4-2.6 2.4.7 3.5L5 7.8 1.9 9.6l.7-3.5L0 3.7l3.5-.4z"/></svg><svg viewBox="0 0 10 10"><path d="M5 0l1.5 3.3 3.5.4-2.6 2.4.7 3.5L5 7.8 1.9 9.6l.7-3.5L0 3.7l3.5-.4z"/></svg><svg viewBox="0 0 10 10"><path d="M5 0l1.5 3.3 3.5.4-2.6 2.4.7 3.5L5 7.8 1.9 9.6l.7-3.5L0 3.7l3.5-.4z"/></svg><svg viewBox="0 0 10 10"><path d="M5 0l1.5 3.3 3.5.4-2.6 2.4.7 3.5L5 7.8 1.9 9.6l.7-3.5L0 3.7l3.5-.4z"/></svg><svg viewBox="0 0 10 10"><path d="M5 0l1.5 3.3 3.5.4-2.6 2.4.7 3.5L5 7.8 1.9 9.6l.7-3.5L0 3.7l3.5-.4z"/></svg></div><h3>Brand New Modern Apartment</h3><div class="loc"><svg width="8" height="10" viewBox="0 0 8 10"><path d="M4 0a3.5 3.5 0 00-3.5 3.5C.5 6 4 10 4 10s3.5-4 3.5-6.5A3.5 3.5 0 004 0z" fill="#ddd"/></svg>Unbeatable Location</div><div class="price">From <b>$150.0</b> &nbsp;/Per Night</div></div></div>

<div class="abs card" style="left:450px;top:1631px"><div class="photo photo-sea" role="img" aria-label="Sea view at dusk from the apartment terrace"></div><div class="shade"></div><div class="info"><div class="stars"><svg viewBox="0 0 10 10"><path d="M5 0l1.5 3.3 3.5.4-2.6 2.4.7 3.5L5 7.8 1.9 9.6l.7-3.5L0 3.7l3.5-.4z"/></svg><svg viewBox="0 0 10 10"><path d="M5 0l1.5 3.3 3.5.4-2.6 2.4.7 3.5L5 7.8 1.9 9.6l.7-3.5L0 3.7l3.5-.4z"/></svg><svg viewBox="0 0 10 10"><path d="M5 0l1.5 3.3 3.5.4-2.6 2.4.7 3.5L5 7.8 1.9 9.6l.7-3.5L0 3.7l3.5-.4z"/></svg><svg viewBox="0 0 10 10"><path d="M5 0l1.5 3.3 3.5.4-2.6 2.4.7 3.5L5 7.8 1.9 9.6l.7-3.5L0 3.7l3.5-.4z"/></svg><svg viewBox="0 0 10 10"><path d="M5 0l1.5 3.3 3.5.4-2.6 2.4.7 3.5L5 7.8 1.9 9.6l.7-3.5L0 3.7l3.5-.4z"/></svg></div><h3>Brand New Modern Apartment</h3><div class="loc"><svg width="8" height="10" viewBox="0 0 8 10"><path d="M4 0a3.5 3.5 0 00-3.5 3.5C.5 6 4 10 4 10s3.5-4 3.5-6.5A3.5 3.5 0 004 0z" fill="#ddd"/></svg>Unbeatable Location</div><div class="price">From <b>$150.0</b> &nbsp;/Per Night</div></div></div>

<div class="abs card" style="left:787px;top:1631px"><div class="photo photo-room" role="img" aria-label="Dark modern living room with sofa"></div><div class="shade"></div><div class="info"><div class="stars"><svg viewBox="0 0 10 10"><path d="M5 0l1.5 3.3 3.5.4-2.6 2.4.7 3.5L5 7.8 1.9 9.6l.7-3.5L0 3.7l3.5-.4z"/></svg><svg viewBox="0 0 10 10"><path d="M5 0l1.5 3.3 3.5.4-2.6 2.4.7 3.5L5 7.8 1.9 9.6l.7-3.5L0 3.7l3.5-.4z"/></svg><svg viewBox="0 0 10 10"><path d="M5 0l1.5 3.3 3.5.4-2.6 2.4.7 3.5L5 7.8 1.9 9.6l.7-3.5L0 3.7l3.5-.4z"/></svg><svg viewBox="0 0 10 10"><path d="M5 0l1.5 3.3 3.5.4-2.6 2.4.7 3.5L5 7.8 1.9 9.6l.7-3.5L0 3.7l3.5-.4z"/></svg><svg viewBox="0 0 10 10"><path d="M5 0l1.5 3.3 3.5.4-2.6 2.4.7 3.5L5 7.8 1.9 9.6l.7-3.5L0 3.7l3.5-.4z"/></svg></div><h3>Brand New Modern Apartment</h3><div class="loc"><svg width="8" height="10" viewBox="0 0 8 10"><path d="M4 0a3.5 3.5 0 00-3.5 3.5C.5 6 4 10 4 10s3.5-4 3.5-6.5A3.5 3.5 0 004 0z" fill="#ddd"/></svg>Unbeatable Location</div><div class="price">From <b>$150.0</b> &nbsp;/Per Night</div></div></div>

<!-- services -->
<div class="abs services"></div>
<h2 class="abs h2 center" style="top:2038px">Our Services</h2>
<p class="abs para center" style="left:130px;top:2108px;width:940px">Ctincidunt ut laoreet dolore magna aliquam erat volutpat. Ut wisi enim ad mini m veniam, quis nostrud exerci tation suscipit lobortis nisl ut aliquip. Ctincidunt ut laoreet dolore magna aliquam erat volutpat.</p>

<div class="abs service" style="left:114px;top:2193px"><div class="icon"><svg viewBox="0 0 24 24"><path d="M3 12l9-9h8v8l-9 9z"/><circle cx="16" cy="8" r="1.5"/></svg></div><h4>Discount Booking</h4><p>Ctincidunt ut la dolore magna aliquam erat volutpat.</p></div>
<div class="abs service" style="left:450px;top:2193px"><div class="icon"><svg viewBox="0 0 24 24"><circle cx="9" cy="14" r="5"/><circle cx="15" cy="14" r="5"/><path d="M9 5l3 3 3-3"/></svg></div><h4>Wedding &amp; Events</h4><p>Ctincidunt ut la dolore magna aliquam erat volutpat.</p></div>
<div class="abs service" style="left:789px;top:2193px"><div class="icon"><svg viewBox="0 0 24 24"><path d="M12 20l-7-7a4.5 4.5 0 017-5.5A4.5 4.5 0 0119 13z"/></svg></div><h4>Services Three</h4><p>Ctincidunt ut la dolore magna aliquam erat volutpat.</p></div>
<div class="abs service" style="left:114px;top:2289px"><div class="icon"><svg viewBox="0 0 24 24"><path d="M3 18h18M5 18a7 7 0 0114 0M12 8v3"/></svg></div><h4>Services Five</h4><p>Ctincidunt ut la dolore magna aliquam erat volutpat.</p></div>
<div class="abs service" style="left:450px;top:2289px"><div class="icon"><svg viewBox="0 0 24 24"><circle cx="12" cy="12" r="8"/><path d="M12 7v5l3 3"/></svg></div><h4>Services Four</h4><p>Ctincidunt ut la dolore magna aliquam erat volutpat.</p></div>
<div class="abs service" style="left:789px;top:2289px"><div class="icon"><svg viewBox="0 0 24 24"><path d="M5 12l4 4 10-10"/></svg></div><h4>Services Six</h4><p>Ctincidunt ut la dolore magna aliquam erat volutpat.</p></div>

<!-- testimonial -->
<div class="abs testi-bg" role="img" aria-label="Blurred view of Prague old town towers"></div>
<h2 class="abs h2 center testi-title">What Customer Say</h2>
<div class="abs quote-box"></div>
<svg class="abs quote-mark" width="30" height="26" viewBox="0 0 30 26"><path d="M0 26V14C0 6 4 1 12 0v5c-4 1-6 4-6 8h6v13zm17 0V14c0-8 4-13 12-14v5c-4 1-6 4-6 8h6v13z" fill="#fff"/></svg>
<p class="abs quote-text center">Ctincidunt ut laoreet dolore magna aliquam erat volutpat. Ut wisi enim ad mini m veniam, quis nostrud exerci tation suscipit lobortis nisl ut aliquip. Ctincidunt ut laoreet dolore magna aliquam erat volutpat. Ut wisi enim ad mini m veniam, quis nostrud exerci tation ullamcorperullamcorper suscipit lobortis nisl.</p>
<div class="abs avatar" role="img" aria-label="Customer portrait"></div>
<div class="abs cust-name">Miss. Customer Name</div>
<div class="abs couple" role="img" aria-label="Happy couple travelling, smiling together"></div>

<!-- newsletter -->
<div class="abs newsletter"></div>
<h2 class="abs h2 center" style="top:3057px">Newsletter Signup</h2>
<p class="abs para center" style="left:130px;top:3129px;width:940px">Ctincidunt ut laoreet dolore magna aliquam erat volutpat. Ut wisi enim ad mini m veniam, quis nostrud exerci tation suscipit lobortis nisl ut aliquip. Ctincidunt ut laoreet dolore magna aliquam erat volutpat.</p>
<div class="abs email">Enter your email address</div>
<div class="abs btn subscribe">Subscribe Now</div>

<!-- footer -->
<footer class="abs footer"></footer>
<h3 class="abs fh" style="left:114px">Get in Touch</h3>
<h3 class="abs fh" style="left:414px">Quick Link</h3>
<h3 class="abs fh" style="left:709px">Gallery</h3>

<div class="abs contact-row" style="left:114px;top:3402px;width:240px"><svg viewBox="0 0 24 24"><path d="M12 2a7 7 0 00-7 7c0 5 7 13 7 13s7-8 7-13a7 7 0 00-7-7zm0 9.5A2.5 2.5 0 1112 6a2.5 2.5 0 010 5.5z"/></svg><div><b>Main Office</b><br>Northgate Property Services dolor lorem Ut wisi enim ad minim.</div></div>
<div class="abs contact-row" style="left:114px;top:3470px"><svg viewBox="0 0 24 24"><path d="M6.6 10.8a15 15 0 006.6 6.6l2.2-2.2c.3-.3.7-.4 1-.2 1.1.4 2.3.6 3.6.6.6 0 1 .4 1 1V20c0 .6-.4 1-1 1A17 17 0 013 4c0-.6.4-1 1-1h3.5c.6 0 1 .4 1 1 0 1.3.2 2.5.6 3.6.1.3 0 .7-.2 1z"/></svg><b style="font-size:14px">123-456-7890</b></div>
<div class="abs contact-row" style="left:114px;top:3500px"><svg viewBox="0 0 24 24"><path d="M2 5h20v14H2zm1 1l9 7 9-7" /></svg>info@northgate.example</div>

<div class="abs links" style="left:414px;top:3396px">Home<br>Apartments<br>Location<br>Services<br>Gallery</div>
<div class="abs links" style="left:522px;top:3396px">News<br>Exclusive Offers &amp; Tours<br>For Families<br>Contact</div>

<div class="abs gal g1" style="left:709px" role="img" aria-label="White bedroom with canopy bed"></div>
<div class="abs gal g2" style="left:837px" role="img" aria-label="Terrace with pool and blue sky"></div>
<div class="abs gal g3" style="left:968px" role="img" aria-label="Villa garden with greenery"></div>

<div class="abs foot-line"></div>
<div class="abs copy center">© All Rights Reserved. 2017</div>

</body>
</html>
```